Design of slide which will later be converted to video

We need slides which will be converted to a video format for web and social media marketing. We are attaching our concept draft as a start

All slides are provided as background only at this point, but if someone has a great idea for any of the other topics, feel free to provide that as well.

Using the attached slides (11-15), please re-create the slides in a more artistic and unified presentation, using stock images of the dog characters (no animation). The Professor must be a Basset hound with glasses; the other dog characters should be similar to the ones used in the slides. Voices and music will be added later. Any detail that can be added to make the video a seamless narrative is encouraged.
Original source files for pics here: quillbarkhaus-my.fileshelf.example/:f:/p/trevor/Kx_R7TQWm_bPlDcVa-hRxZAqQv3Lseyfm9Tk04B7W1Nj?e=QWPLMA
Updates

We have updated our brief to include source files for our images. Many designers have asked for this. Please have a look!

Target Market(s)

Fresh Pet Food

Industry/Entity Type

Pet Food

Colors
EB3D1F
EC4F4E
F09395
F8D3D4
FCEDEE

Requirements
Must have
• We want to keep the picture of the basset hound with glasses. We can potentially use other pictures of the other dogs, but not necessary. All dogs must be real pictures, no animation! The chalkboard needs to be a chalkboard - do not change it to something else, but please feel free to improve its look. This improvement - to all of our graphics - is what we are looking for.
Nice to have
• The chalkboard text come in as being written in real time; the dog pictures selected can be changed as per the designder creative instincts. We are pretty committed to the Basset Hound playing Professor Wembleton, but we are always open to suggestion

```html
<!DOCTYPE html>
<html lang="en">
<head>
<meta charset="utf-8">
<title>Vellora – Canine Diet Slides</title>
<link href="https://fonts.googleapis.com/css2?family=Montserrat:wght@600;700;800&display=swap" rel="stylesheet">
<style>
  :root{
    --board:#cdcdcd;
    --slide:#ffffff;
    --brand-red:#b1241c;
    --ink:#111111;
    --chalk-green:#4d7a52;
    --wood:#b8561f;
    --wood-dark:#7e3410;
    --fur-light:#c98a55;
    --fur-dark:#6b3a1c;
    --puppy:#e6c18f;
    --mic:#2a2a2a;
  }
  *{box-sizing:border-box;margin:0;padding:0}
  html,body{width:1200px;height:1000px;overflow:hidden;background:var(--board);font-family:"Montserrat",sans-serif}
  .storyboard{position:relative;width:1200px;height:1000px}
  .slide{position:absolute;width:537px;height:302px;background:var(--slide);box-shadow:6px 7px 6px rgba(0,0,0,.35);overflow:hidden}
  .photo{position:absolute;z-index:0;border-radius:42% 42% 14% 14%}
  .photo.basset{background:radial-gradient(ellipse at 50% 35%,var(--fur-light),var(--fur-dark) 78%,rgba(255,255,255,0) 100%)}
  .photo.puppy{background:radial-gradient(ellipse at 50% 45%,var(--puppy),#c89a63 72%,rgba(255,255,255,0) 100%)}
  .photo.mic{background:linear-gradient(180deg,#444,var(--mic));border-radius:5px;width:9px}
  .slide-art{position:absolute;inset:0;width:537px;height:302px;z-index:1}
  .slide-title{position:absolute;z-index:2;left:24px;top:16px;color:#fff;font-weight:700;font-size:17px;letter-spacing:1.2px;text-transform:uppercase;line-height:24px}
  .brand-mark{position:absolute;z-index:2;right:18px;top:22px;display:flex;align-items:center;gap:4px;color:var(--brand-red);font-weight:800;font-size:11px}
  .brand-mark .dot{width:10px;height:10px;border-radius:50%;background:var(--brand-red)}
  .bubble-text{position:absolute;z-index:2;text-align:center;font-weight:800;color:var(--ink);display:flex;align-items:center;justify-content:center;line-height:1.25}
  .caption{position:absolute;z-index:2;font-size:10.5px;font-weight:600;color:var(--ink)}
  .slide-number{position:absolute;z-index:2;right:22px;bottom:16px;width:28px;height:28px;border-radius:50%;background:var(--ink);color:#fff;font-weight:700;font-size:15px;display:flex;align-items:center;justify-content:center}
  .chalkboard{position:absolute;z-index:1;left:24px;top:80px;width:354px;height:204px;background:var(--wood);border:3px solid var(--wood-dark);padding:10px}
  .chalkboard-surface{width:100%;height:100%;background:var(--chalk-green);padding:4px 8px;display:flex;flex-direction:column;gap:4px}
  .chalk-row{display:flex;gap:10px;align-items:flex-start;flex:1}
  .chalk-icon{width:56px;height:55px;flex:none;border:2px solid #fff;background:linear-gradient(180deg,#1b1b1b 60%,#b12b24)}
  .chalk-row p{color:#fff;font-size:7.6px;font-weight:700;line-height:1.35;padding-top:6px}
  .revolution-text{font-size:12.5px;line-height:1.35}
  .revolution-text .brand{color:var(--brand-red);white-space:nowrap}
  .revolution-text .brand::before{content:"";display:inline-block;width:11px;height:11px;border-radius:50%;background:var(--brand-red);margin-right:4px;vertical-align:-1px}
</style>
</head>
<body>
<main class="storyboard">

  <section class="slide slide-lifespan" style="left:54px;top:25px">
    <div class="photo basset" role="img" aria-label="Photo of a basset hound wearing round glasses, sitting" style="left:318px;top:20px;width:176px;height:254px"></div>
    <svg class="slide-art" viewBox="0 0 537 302" aria-hidden="true">
      <path d="M0 0H350C362 28 338 52 300 57C220 66 120 46 60 56C30 61 10 70 0 76Z" fill="var(--brand-red)"/>
      <ellipse cx="166" cy="178" rx="114" ry="64" fill="#fff" stroke="var(--brand-red)" stroke-width="4"/>
      <path d="M230 222L268 248L250 214" fill="#fff" stroke="var(--brand-red)" stroke-width="4" stroke-linejoin="round"/>
    </svg>
    <h2 class="slide-title">Canine Diet and Life Span</h2>
    <div class="brand-mark"><span class="dot"></span>Vellora</div>
    <div class="bubble-text" style="left:60px;top:128px;width:212px;height:100px;font-size:19px">Ask Professor<br>Wembleton</div>
    <p class="caption" style="left:331px;top:278px">The World Smartest Dog</p>
  </section>

  <section class="slide slide-question" style="left:613px;top:25px">
    <div class="photo mic" role="img" aria-label="Photo of a microphone on a stand" style="left:290px;top:100px;height:170px"></div>
    <div class="photo puppy" role="img" aria-label="Photo of a golden retriever puppy speaking into the microphone" style="left:336px;top:58px;width:176px;height:180px"></div>
    <svg class="slide-art" viewBox="0 0 537 302" aria-hidden="true">
      <path d="M0 0H350C362 28 338 52 300 57C220 66 120 46 60 56C30 61 10 70 0 76Z" fill="var(--brand-red)"/>
      <ellipse cx="158" cy="172" rx="112" ry="74" fill="#fff" stroke="var(--brand-red)" stroke-width="4"/>
      <path d="M240 200L278 214L248 186" fill="#fff" stroke="var(--brand-red)" stroke-width="4" stroke-linejoin="round"/>
      <ellipse cx="392" cy="246" rx="58" ry="40" fill="#fff" stroke="var(--brand-red)" stroke-width="4"/>
      <path d="M350 220L340 168L366 210" fill="#fff" stroke="var(--brand-red)" stroke-width="4" stroke-linejoin="round"/>
    </svg>
    <h2 class="slide-title">Ask Question</h2>
    <div class="brand-mark"><span class="dot"></span>Vellora</div>
    <div class="bubble-text" style="left:56px;top:112px;width:204px;height:120px;font-size:19px">Professor<br>Wembleton,<br>How Can Dog<br>Live Longer?</div>
    <div class="bubble-text" style="left:338px;top:214px;width:108px;height:64px;font-size:18px">Healthier<br>Lives?</div>
    <div class="slide-number">2</div>
  </section>

  <section class="slide slide-history" style="left:54px;top:353px">
    <div class="photo basset" role="img" aria-label="Photo of a basset hound in glasses lying down, tongue out" style="left:296px;top:40px;width:200px;height:238px"></div>
    <svg class="slide-art" viewBox="0 0 537 302" aria-hidden="true">
      <path d="M0 0H350C362 28 338 52 300 57C220 66 120 46 60 56C30 61 10 70 0 76Z" fill="var(--brand-red)"/>
      <ellipse cx="166" cy="164" rx="116" ry="80" fill="#fff" stroke="var(--brand-red)" stroke-width="4"/>
      <path d="M246 206L290 214L258 188" fill="#fff" stroke="var(--brand-red)" stroke-width="4" stroke-linejoin="round"/>
    </svg>
    <h2 class="slide-title">Canine Diet History</h2>
    <div class="brand-mark"><span class="dot"></span>Vellora</div>
    <div class="bubble-text" style="left:66px;top:100px;width:200px;height:128px;font-size:19px">Lets Take A<br>Look At The<br>History Of<br>Canine Diets</div>
    <p class="caption" style="left:331px;top:280px">The World Smartest Dog</p>
    <div class="slide-number">3</div>
  </section>

  <section class="slide slide-effects" style="left:613px;top:353px">
    <svg class="slide-art" viewBox="0 0 537 302" aria-hidden="true">
      <path d="M0 0H350C364 34 342 62 300 66C220 74 120 60 60 66C30 69 10 72 0 76Z" fill="var(--brand-red)"/>
    </svg>
    <h2 class="slide-title" style="top:12px;line-height:23px">Effects of Modern Diet<br>on Dogs</h2>
    <div class="brand-mark"><span class="dot"></span>Vellora</div>
    <div class="chalkboard">
      <div class="chalkboard-surface">
        <div class="chalk-row"><div class="chalk-icon" role="img" aria-label="Dog silhouette eating from a bowl"></div><p>Up until the modern age, the domestic dog ate what his master ate---bones and scraps from the family table---and enjoyed a long life, often spanning two (2) decades.</p></div>
        <div class="chalk-row"><div class="chalk-icon" role="img" aria-label="Dog silhouette eating from a bowl"></div><p>Since the 1950's, however dogs have been fed what cows ate---a corn based diet. As a result, over 80% of modern dogs have gum disease and over half of dogs 10 y/o or older will develop cancer.</p></div>
        <div class="chalk-row"><div class="chalk-icon" role="img" aria-label="Dog silhouette eating from a bowl"></div><p>In the 1990's marketeers un-scientifically pushed a wolf diet, with too much protein and too little fiber, causing dogs to become overweight and yet still be hungry.</p></div>
      </div>
    </div>
    <div class="photo basset" role="img" aria-label="Photo of a basset hound in glasses beside the chalkboard" style="left:362px;top:118px;width:150px;height:168px;z-index:2"></div>
    <div class="slide-number" style="z-index:3">4</div>
  </section>

  <section class="slide slide-revolution" style="left:54px;top:676px">
    <div class="photo basset" role="img" aria-label="Photo of a basset hound wearing round glasses, sitting" style="left:318px;top:20px;width:176px;height:254px"></div>
    <svg class="slide-art" viewBox="0 0 537 302" aria-hidden="true">
      <path d="M0 0H350C362 28 338 52 300 57C220 66 120 46 60 56C30 61 10 70 0 76Z" fill="var(--brand-red)"/>
      <ellipse cx="198" cy="164" rx="114" ry="76" fill="#fff" stroke="var(--brand-red)" stroke-width="4"/>
      <path d="M290 196L330 192L300 176" fill="#fff" stroke="var(--brand-red)" stroke-width="4" stroke-linejoin="round"/>
    </svg>
    <h2 class="slide-title">Join the Revolution</h2>
    <div class="brand-mark"><span class="dot"></span>Vellora</div>
    <div class="bubble-text revolution-text" style="left:94px;top:96px;width:208px;height:136px">
      <div>Join The<br><span class="brand">Vellora Superfood</span><br>Revolution Today!<br>Give Your Pet The Food<br>Best Formulated<br>To Satisfy The<br>Total Dog.</div>
    </div>
    <p class="caption" style="left:331px;top:278px">The World Smartest Dog</p>
    <div class="slide-number">5</div>
  </section>

</main>
</body>
</html>
```